Accountant services flyer & marketing portfolio

I require a design for a marketing portfolio of blank templates for a flyer, product brochure, report cover for A4 based on our style - current logo, letterhead, website look and feel - that can be updated in publisher or word with relevant marketing and company information editorial material and text. It will be either printed A4 or saved as PDF and distributed

Target Market(s)

small business and investment / superfund clients

Industry/Entity Type

Accountant

Font styles to use
Sans Serif

Requirements
Must have
• Instyle of letterhead and website
Professional body logos
Space to input text
Relevant happy images
Nice to have
• Images of happy lifestyle types retirees, young families and mid-aged
tradesmen and professionals

```html
<!DOCTYPE html>
<html lang="en">
<head>
<meta charset="utf-8">
<title>Meridian Advisory – Folder Cover and Inner Spread</title>
<link rel="stylesheet" href="https://fonts.googleapis.com/css2?family=Montserrat:wght@400;500;600;700;800&display=swap">
<style>
  :root{
    --orange:#f0782a;
    --orange-deep:#e0461c;
    --orange-light:#f7a03a;
    --ink:#2b2b2b;
    --muted:#555;
    --grey-pale:#f1f1f2;
    --grey-soft:#e3e3e5;
    --stage:#ececee;
    --white:#fff;
  }
  html,body{margin:0;padding:0;overflow:hidden}
  body{width:1200px;height:2700px;background:var(--stage);position:relative;font-family:"Montserrat",sans-serif}
  .spread{position:absolute;left:40px;width:1120px;height:797px;display:block;background:var(--white);box-shadow:0 2px 6px rgba(0,0,0,.08)}
  .spread--cover{top:508px}
  .spread--inner{top:1395px}
  text{font-family:"Montserrat",sans-serif}
  .brand-name{font-weight:500;fill:var(--orange-deep)}
  .brand-name--light{fill:var(--white)}
  .headline{font-weight:800;fill:var(--white)}
  .subhead{font-weight:700;fill:var(--white)}
  .contact{font-weight:600;fill:var(--white)}
  .kicker{font-weight:700;fill:var(--ink)}
  .section-title{font-weight:400;fill:var(--ink)}
  .section-title .accent{font-weight:700;fill:var(--orange-deep)}
  .body-copy{font-weight:400;fill:var(--muted)}
  .card-title{font-weight:700;fill:var(--ink)}
  .card-title--accent{font-weight:700;fill:var(--orange-deep)}
  .card-copy{font-weight:400;fill:var(--muted)}
  .service-title{font-weight:700;fill:var(--ink)}
  .footer-link{font-weight:600;fill:var(--orange-deep)}
  .page-num{font-weight:700;fill:var(--ink)}
</style>
</head>
<body>

<!-- Folder cover: back (left) and front (right) -->
<svg class="spread spread--cover" viewBox="0 0 652 464" aria-label="Folder cover spread">
  <defs>
    <linearGradient id="coverOrange" x1="0" y1="0" x2="1" y2="0">
      <stop offset="0" stop-color="var(--orange-deep)"/>
      <stop offset="1" stop-color="var(--orange-light)"/>
    </linearGradient>
    <linearGradient id="ringOrange" x1="0" y1="0" x2="1" y2="1">
      <stop offset="0" stop-color="var(--orange-deep)"/>
      <stop offset="1" stop-color="var(--orange-light)"/>
    </linearGradient>
    <linearGradient id="greyWash" x1="0" y1="0" x2="1" y2="1">
      <stop offset="0" stop-color="#e6e6e8"/>
      <stop offset="1" stop-color="#f7f7f8"/>
    </linearGradient>
  </defs>

  <rect class="page-bg" x="0" y="0" width="652" height="464" fill="var(--white)"/>
  <rect class="back-photo" x="0" y="0" width="330" height="320" fill="url(#greyWash)" role="img" aria-label="Faded black and white photo of a desk with tablet, papers and a magnifying glass"/>

  <path class="cover-wave" d="M0 250 C70 300 200 330 290 305 C340 290 365 255 400 235 C470 195 560 150 652 100 L652 464 L0 464 Z" fill="url(#coverOrange)"/>
  <path class="cover-swoosh" d="M0 244 C70 292 200 322 288 298 C338 284 362 250 398 229" fill="none" stroke="var(--orange-light)" stroke-width="2" opacity=".8"/>

  <circle class="photo-ring" cx="490" cy="220" r="120" fill="url(#ringOrange)"/>
  <circle class="photo-ring-gap" cx="490" cy="220" r="113" fill="var(--white)"/>
  <circle class="team-photo" cx="490" cy="220" r="108" fill="#c9ccd1" role="img" aria-label="Overhead photo of business people reviewing charts and a laptop at a white table"/>

  <circle class="brand-dot" cx="490" cy="44" r="12" fill="none" stroke="var(--orange-deep)" stroke-width="3"/>
  <text class="brand-name" x="490" y="76" font-size="12.5" text-anchor="middle">MERIDIAN ADVISORY</text>

  <text class="headline" x="490" y="385" font-size="21" text-anchor="middle">THINK! TECHNOLOGY</text>
  <text class="subhead" x="490" y="401" font-size="8.6" text-anchor="middle">THE DIGITAL REVOLUTION HAS BEGUN</text>
  <text class="subhead" x="490" y="413" font-size="8.6" text-anchor="middle">EMBRACE THE OPPORTUNITY!</text>
  <line x1="360" y1="423" x2="620" y2="423" stroke="var(--white)" stroke-width=".6" opacity=".8"/>
  <rect x="480" y="421.5" width="20" height="3" fill="var(--white)"/>
  <text class="contact" x="490" y="442" font-size="6.6" text-anchor="middle">www.meridianadvisory.com.au</text>

  <circle class="brand-dot" cx="165" cy="352" r="12" fill="none" stroke="var(--white)" stroke-width="3"/>
  <text class="brand-name brand-name--light" x="165" y="390" font-size="11.5" text-anchor="middle">MERIDIAN ADVISORY</text>

  <g class="contact-block">
    <path d="M19 417 q1 -2 3 -1 l1 2 q-1 1 0 2 l1 1 q1 1 2 0 l2 1 q1 2 -1 3 q-4 0 -8 -8 z" fill="var(--white)"/>
    <text class="contact" x="32" y="423" font-size="5.8">1300 555 014 / 0400 555 321</text>
    <path d="M23 431 a3 3 0 0 1 3 3 q0 2 -3 6 q-3 -4 -3 -6 a3 3 0 0 1 3 -3 z" fill="var(--white)"/>
    <text class="contact" x="32" y="436" font-size="5.8">Suite 204, Level 2, 48 Harbour Drive</text>
    <text class="contact" x="32" y="445" font-size="5.8">Lakeside NSW 2999</text>
    <rect x="187" y="418" width="7" height="5" fill="var(--white)"/>
    <text class="contact" x="197" y="423" font-size="5.8">hello@meridianadvisory.com.au</text>
    <circle cx="190.5" cy="438" r="3" fill="none" stroke="var(--white)" stroke-width=".9"/>
    <text class="contact" x="197" y="440" font-size="5.8">www.meridianadvisory.com.au</text>
  </g>
</svg>

<!-- Inner spread: About (left) and Services (right) -->
<svg class="spread spread--inner" viewBox="0 0 652 464" aria-label="Folder inner spread">
  <rect class="page-bg" x="0" y="0" width="652" height="464" fill="var(--white)"/>

  <polygon class="city-photo" points="0,0 345,0 318,55 0,55" fill="#4a2b16" role="img" aria-label="Night photo of a lit city skyline"/>
  <polygon class="header-slash" points="345,0 353,0 326,55 318,55" fill="var(--orange-deep)"/>
  <rect x="350" y="1" width="302" height="3" fill="var(--ink)"/>
  <rect x="348" y="5.5" width="304" height="1.5" fill="var(--orange-deep)"/>

  <!-- About page -->
  <text class="kicker" x="21" y="76" font-size="6.2">DANIEL MORROW - MERIDIAN ADVISORY</text>
  <text class="section-title" x="21" y="95" font-size="13.5">ABOUT <tspan class="accent">MERIDIAN</tspan></text>
  <g class="body-copy" font-size="5.6">
    <text x="21" y="114">For over 35 years Meridian CEO Daniel Morrow has prospered on the "Cutting</text>
    <text x="21" y="121.5">Edge" of Business and Finance. With extensive qualifications, comprehensive</text>
    <text x="21" y="129">and wide ranging hands-on experience, he offers a unique and potent</text>
    <text x="21" y="136.5">combination of expertise and knowledge that will guarantee superior strategic</text>
    <text x="21" y="144">advice that can really make a difference.</text>
  </g>

  <g class="card-grid">
    <rect x="23" y="164" width="78" height="58" fill="#9aa3ad" role="img" aria-label="Photo of a hand wearing a smartwatch"/>
    <rect x="126" y="164" width="78" height="58" fill="#8b8f96" role="img" aria-label="Photo of a hand holding a smartphone over a laptop"/>
    <rect x="227" y="164" width="78" height="58" fill="#a9b4c2" role="img" aria-label="Photo of a historic stone gate under a blue sky"/>
    <rect x="23" y="292" width="78" height="58" fill="#7d8a6a" role="img" aria-label="Portrait photo of the company CEO"/>
    <rect x="126" y="292" width="78" height="58" fill="#a08a78" role="img" aria-label="Photo of team hands stacked together"/>
    <rect x="227" y="292" width="78" height="58" fill="#3556b8" role="img" aria-label="Photo of a blue digital financial display"/>

    <g text-anchor="middle" font-size="6.4">
      <text class="card-title" x="62" y="237">WELCOME TO</text>
      <text class="card-title--accent" x="62" y="246">CLIENTS</text>
      <text class="card-title" x="165" y="237">OUR</text>
      <text class="card-title--accent" x="165" y="246">VISION</text>
      <text class="card-title" x="266" y="237">HISTORY &amp;</text>
      <text class="card-title--accent" x="266" y="246">ACHIEVEMENTS</text>
      <text class="card-title" x="62" y="365">CEO DANIEL</text>
      <text class="card-title--accent" x="62" y="374">MORROW</text>
      <text class="card-title" x="165" y="365">OUR POINT OF</text>
      <text class="card-title--accent" x="165" y="374">DIFFERENCE</text>
      <text class="card-title" x="266" y="365">JOBMAKER</text>
      <text class="card-title--accent" x="266" y="374">HIRING CREDIT</text>
    </g>
    <g class="card-copy" text-anchor="middle" font-size="3.6">
      <text x="62" y="254">Since launch we have guided local owners</text>
      <text x="62" y="259">toward sound accounting, wealth and</text>
      <text x="62" y="264">business advisory outcomes.</text>
      <text x="165" y="254">The digital revolution keeps reshaping</text>
      <text x="165" y="259">how firms work, and the next decade</text>
      <text x="165" y="264">will bring even deeper change.</text>
      <text x="266" y="254">Our practice carries a rich vein of</text>
      <text x="266" y="259">qualifications, expertise and client</text>
      <text x="266" y="264">care built over many years.</text>
      <text x="62" y="382">I find it rewarding to help clients</text>
      <text x="62" y="387">reach their personal, family</text>
      <text x="62" y="392">and business goals.</text>
      <text x="165" y="382">We deliver full-service accounting</text>
      <text x="165" y="387">and advice, with a complete</text>
      <text x="165" y="392">suite of business and personal</text>
      <text x="165" y="397">investment solutions.</text>
      <text x="266" y="382">Find out if your business is eligible</text>
      <text x="266" y="387">for the hiring credit scheme.</text>
      <text x="266" y="392">Read the guide online.</text>
    </g>
  </g>

  <g class="page-footer">
    <circle cx="24" cy="434" r="7" fill="none" stroke="var(--orange-deep)" stroke-width="2"/>
    <text class="brand-name" x="35" y="437" font-size="5.6">MERIDIAN ADVISORY</text>
    <rect x="100" y="438" width="192" height="2" fill="var(--orange-deep)"/>
    <text class="footer-link" x="290" y="435" font-size="3.6" text-anchor="end">www.meridianadvisory.com.au</text>
    <circle cx="302" cy="439" r="6.5" fill="var(--white)" stroke="var(--ink)" stroke-width=".7"/>
    <text class="page-num" x="302" y="441.5" font-size="6.5" text-anchor="middle">1</text>
  </g>

  <!-- Services page -->
  <text class="kicker" x="346" y="33" font-size="6.2">DANIEL MORROW - MERIDIAN ADVISORY</text>
  <text class="section-title" x="346" y="51" font-size="13.5">OUR <tspan class="accent">SERVICES</tspan></text>
  <g class="body-copy" font-size="5.4">
    <text x="346" y="64">Meridian Advisory is uniquely positioned to offer an unparalleled range of financial</text>
    <text x="346" y="71">advice that incorporates both Business and Personal financial growth strategies.</text>
  </g>

  <g class="service-icons" fill="none" stroke="var(--orange-deep)">
    <circle cx="360" cy="96" r="10" stroke-width="1.4"/><circle cx="360" cy="96" r="6.5" stroke-width=".8"/>
    <circle cx="360" cy="143" r="10" stroke-width="1.4"/><circle cx="360" cy="143" r="6.5" stroke-width=".8"/>
    <circle cx="360" cy="188" r="10" stroke-width="1.4"/><circle cx="360" cy="188" r="6.5" fill="var(--orange-deep)" stroke="none"/>
    <circle cx="508" cy="96" r="10" stroke-width="1.4"/><circle cx="508" cy="96" r="6.5" stroke-width=".8"/>
    <circle cx="508" cy="137" r="10" stroke-width="1.4"/><circle cx="508" cy="137" r="6.5" stroke-width=".8"/>
    <circle cx="508" cy="182" r="10" stroke-width="1.4"/><circle cx="508" cy="182" r="6.5" stroke-width=".8"/>
  </g>

  <g font-size="5.2">
    <text class="service-title" x="383" y="91">TAX &amp; ACCOUNTING</text>
    <g class="body-copy"><text x="383" y="99">With extensive taxation</text><text x="383" y="106">experience and an</text><text x="383" y="113">enviable network of</text><text x="383" y="120">Expert Consultants...</text></g>

    <text class="service-title" x="383" y="143">Litigation, Audit &amp;</text>
    <text class="service-title" x="383" y="150">Assurance</text>
    <g class="body-copy"><text x="383" y="159">The areas of expertise and</text><text x="383" y="166">experience include the</text><text x="383" y="173">following: Expert Witness</text><text x="383" y="180">Business Valuations...</text></g>

    <text class="service-title" x="383" y="193">Outsource CFO Services</text>
    <g class="body-copy"><text x="383" y="203">Business is demanding:</text><text x="383" y="210">Business is dynamic. It's</text><text x="383" y="217">challenging on a daily</text><text x="383" y="224">basis. The business owner</text><text x="383" y="231">is often caught in the</text><text x="383" y="238">detail, trials and aloneness</text><text x="383" y="245">of this landscape. Most</text><text x="383" y="252">would benefit...</text></g>

    <text class="service-title" x="531" y="91">Business Improvement</text>
    <text class="service-title" x="531" y="98">Strategies</text>
    <g class="body-copy"><text x="531" y="106">As the majority partner in</text><text x="531" y="113">a Business Coaching and</text><text x="531" y="120">development business...</text></g>

    <text class="service-title" x="531" y="135">Superannuation &amp;</text>
    <text class="service-title" x="531" y="142">Financial Planning</text>
    <g class="body-copy"><text x="531" y="150">Daniel has been helping</text><text x="531" y="157">clients grow, diversify</text><text x="531" y="164">and protect family</text><text x="531" y="171">wealth...</text></g>

    <text class="service-title" x="531" y="180">BUSINESS</text>
    <text class="service-title" x="531" y="187">RECONSTRUCTION</text>
    <text class="service-title" x="531" y="194">SERVICES</text>
    <g class="body-copy"><text x="531" y="203">The Australian Federal</text><text x="531" y="210">Government announced</text><text x="531" y="217">COVID-19 reforms in October</text><text x="531" y="224">2020 aimed at assisting small</text><text x="531" y="231">businesses to restructure</text><text x="531" y="238">when in financial distress.</text><text x="531" y="245">The reforms were aimed at</text><text x="531" y="252">reducing the complexity and</text></g>
  </g>

  <text class="section-title" x="346" y="306" font-size="13">E-<tspan class="accent">TRENDING</tspan></text>
  <g class="body-copy" font-size="5.4">
    <text x="346" y="320">Here's what we think is trending in the Business &amp; Investment world and our take on</text>
    <text x="346" y="327">the current trends and developments for business and investor clients.</text>
  </g>

  <rect class="trend-panel" x="346" y="337" width="294" height="66" fill="var(--grey-pale)"/>
  <line x1="444" y1="348" x2="444" y2="396" stroke="var(--grey-soft)" stroke-width=".8"/>
  <line x1="542" y1="348" x2="542" y2="396" stroke="var(--grey-soft)" stroke-width=".8"/>
  <g class="trend-icons">
    <circle cx="400" cy="356" r="6.5" fill="var(--orange-deep)"/><rect x="397" y="353.5" width="6" height="4" fill="none" stroke="var(--white)" stroke-width=".8"/>
    <circle cx="497" cy="356" r="6.5" fill="var(--orange-deep)"/><path d="M494 355 l4 -2.5 v6 l-4 -2.5 z" fill="var(--white)"/>
    <circle cx="594" cy="356" r="6.5" fill="var(--orange-deep)"/><rect x="591" y="353" width="6" height="6" fill="none" stroke="var(--white)" stroke-width=".8"/>
  </g>
  <g text-anchor="middle" font-size="4.6">
    <text class="service-title" x="400" y="372">The Digital Revolution</text>
    <text class="service-title" x="497" y="372">Superannuation: Recent News</text>
    <text class="service-title" x="497" y="378">&amp; Announcements</text>
    <text class="service-title" x="594" y="372">Preparing for the</text>
    <text class="service-title" x="594" y="378">2020 Tax Year</text>
  </g>
  <g class="card-copy" text-anchor="middle" font-size="3.1">
    <text x="400" y="381">Sweeping changes are reshaping business.</text>
    <text x="400" y="385.5">Are you ready for what comes next?</text>
    <text x="400" y="390">Click here for more details.</text>
    <text x="497" y="386">Super rules keep shifting each year.</text>
    <text x="497" y="390.5">Make sure your fund works</text>
    <text x="497" y="395">as hard as you do.</text>
    <text x="594" y="386">Tax time is here again. Learn</text>
    <text x="594" y="390.5">what you need to prepare</text>
    <text x="594" y="395">for this year's return.</text>
  </g>

  <g class="page-footer">
    <circle cx="352" cy="434" r="7" fill="none" stroke="var(--orange-deep)" stroke-width="2"/>
    <text class="brand-name" x="363" y="437" font-size="5.6">MERIDIAN ADVISORY</text>
    <rect x="428" y="438" width="192" height="2" fill="var(--orange-deep)"/>
    <text class="footer-link" x="618" y="435" font-size="3.6" text-anchor="end">www.meridianadvisory.com.au</text>
    <circle cx="630" cy="439" r="6.5" fill="var(--white)" stroke="var(--ink)" stroke-width=".7"/>
    <text class="page-num" x="630" y="441.5" font-size="6.5" text-anchor="middle">2</text>
  </g>
</svg>

</body>
</html>
```